Mortgage Broking boutique Business

I’m wanting a revamped look to my existing business card design. I do like the black and silver but happy to have other colours introduced based on your creation. I’ve attached a copy of my current card so you can have a starting point updated details noted brloe. I deal with high net worth individuals so need my card to be sophisticated, classy that gives off a classy vibe

Target Market(s)

High net worth, wealthy

Industry/Entity Type

Mortgage Brokerage

Contact Information for Business Card

Job title: Finance Executive
Phone: +61 7 3287 4419
Mobile: 0471 352 608
Email: marcus@quillbrookcapital.com.au
Web: www.quillbrookcapital.com.au
Address: level 36 Tindale Court, 58 Harwick St Brisbane QLD 4000

Font styles to use
Other font styles liked:
• Helvetica

Colors

Designer to choose colors to be used in the design.

Requirements
Must have
• Use my existing card design as a starting point

```html
<!DOCTYPE html>
<html lang="en">
<head>
<meta charset="utf-8">
<title>Quillbrook Capital — Business Card</title>
<link href="https://fonts.googleapis.com/css2?family=Montserrat:wght@400;500&display=swap" rel="stylesheet">
<style>
  :root {
    --stage: #1c1c1c;
    --card: #0b0b0b;
    --card-glow: #1a1a1a;
    --silver: #d4d4d4;
    --silver-soft: #a9a9a9;
    --white: #f4f4f4;
  }
  html, body {
    margin: 0;
    padding: 0;
    width: 1200px;
    height: 1200px;
    overflow: hidden;
    background: var(--stage);
    font-family: "Montserrat", "Helvetica Neue", Arial, sans-serif;
  }
  .canvas {
    position: relative;
    width: 1200px;
    height: 1200px;
  }
  .card {
    position: absolute;
    left: 150px;
    width: 900px;
    height: 514px;
    background: radial-gradient(ellipse at 50% 35%, var(--card-glow) 0%, var(--card) 70%);
    box-shadow: 0 18px 40px rgba(0,0,0,0.55);
    box-sizing: border-box;
  }
  .card--front { top: 70px; }
  .card--back { top: 616px; }

  .company-name {
    margin: 0;
    color: var(--silver);
    font-weight: 400;
    white-space: nowrap;
  }
  .card--front .company-name {
    position: absolute;
    top: 200px;
    left: 0;
    right: 0;
    text-align: center;
    font-size: 44px;
  }
  .card--back .company-name {
    position: absolute;
    top: 80px;
    right: 70px;
    font-size: 34px;
  }

  .front-web {
    position: absolute;
    bottom: 70px;
    left: 0;
    right: 0;
    text-align: center;
    color: var(--silver);
    font-size: 17px;
    letter-spacing: 6px;
    text-transform: uppercase;
    font-weight: 400;
  }

  .person {
    position: absolute;
    left: 70px;
    top: 230px;
  }
  .person__name {
    margin: 0;
    color: var(--white);
    font-size: 34px;
    font-weight: 500;
    letter-spacing: 4px;
    text-transform: uppercase;
  }
  .person__title {
    margin: 4px 0 0;
    color: var(--silver);
    font-size: 17px;
    font-weight: 400;
    letter-spacing: 5px;
    text-transform: uppercase;
  }
  .contact {
    margin: 22px 0 0;
    padding: 0;
    list-style: none;
    color: var(--white);
    font-size: 19px;
    font-weight: 400;
    line-height: 1.55;
    white-space: nowrap;
  }
  .contact__label { color: var(--silver-soft); }
  .contact__sep { color: var(--silver-soft); padding: 0 6px; }
</style>
</head>
<body>
<main class="canvas">
  <section class="card card--front" aria-label="Card front">
    <p class="company-name">Quillbrook Capital</p>
    <div class="front-web">www.quillbrookcapital.com.au</div>
  </section>

  <section class="card card--back" aria-label="Card back">
    <p class="company-name">Quillbrook Capital</p>
    <div class="person">
      <h1 class="person__name">Marcus Reid</h1>
      <p class="person__title">Finance Executive</p>
      <ul class="contact">
        <li><span class="contact__label">Mobile :</span> 0471 352 608<span class="contact__sep">|</span><span class="contact__label">Office :</span> +61 7 3287 4419</li>
        <li>marcus@quillbrookcapital.com.au<span class="contact__sep">|</span>www.quillbrookcapital.com.au</li>
        <li>level 36 Tindale Court, 58 Harwick St Brisbane QLD 4000</li>
      </ul>
    </div>
  </section>
</main>
</body>
</html>
```